Bright Meridian Partners boutique mgt consulting group 5 page web design

I need a 4 - 5 page website that professionally presents the business and what we do/ offer to potential clients. We are a boutique based consultancy business that is cutting edge, focuses on revenue and profit acceleration for our customers primarily focused on (but looking to expand outside of ) the consumer goods and property/ building markets. We are passionate about seeing our clients grow their business and our Experts are not traditional consultants, rather are senior executive experts that specialise in sales, marketing, leadership, coaching, supply chain functions at C suite and below.

I have just had a new logo created and so would like to replicate this feel through the website please.

The final Website design needs to communicate a new era of consulting and freelance experts where technology will support our offer.. it needs to be be on trend, animated, modern, professional and primarily researched by clients on their mobile devices. Whilst a consultancy I don't want our clients to feel it looks the same as a traditional consultancy...

Videos will be added later.

For basic content feel please see existing www.brightmeridianpartners.example website.
I would expect a landing page, our services, about us/ who we are, clients we work with.

The type of website I like the feel of is:
http://cartlumen.example.com.au

Target Market(s)

Business to Business Manufacturers/ Retailers/ Property

Industry/Entity Type

Management Consulting

Coding

Coded - Design and coding required

Number of Pages Required

5+ page

Font styles to use
Sans Serif

Colors

Designer to choose colors to be used in the design.

Requirements
Must have
• 5 pages including landing page, our services, about us/ who we are, clients we work with.
• Modern, professional look
• demonstrate the services
• ability to add video and content later
• Use the logo
• ability to scroll and look up on mobile devices
Nice to have
• Use my logo as watermark
• Moving images
• I like this website:
• https://trovanix.example
• http://cartlumen.example.com.au
• other websites :
• https://skillharbor.example
Should not have
• The look of a traditional Big 4 consulting firm
• Be fixed and static website

```html
<!DOCTYPE html>
<html lang="en">
<head>
<meta charset="utf-8">
<title>Bright Meridian Partners</title>
<link rel="stylesheet" href="https://fonts.googleapis.com/css2?family=Exo+2:wght@400;500;600;700&family=Ubuntu:wght@400;500&display=swap">
<style>
:root{
  --navy:#1c4886;
  --navy-dark:#163a6e;
  --ink:#222;
  --soft:#f2f1f3;
  --card-soft:#e4e9f1;
  --news:#5a5a5a;
  --footer:#ececec;
  --copy:#d9d9d9;
  --white:#fff;
}
*{box-sizing:border-box;margin:0;padding:0}
html,body{width:1200px;height:3005px;overflow:hidden}
body{font-family:"Ubuntu",sans-serif;color:var(--ink);background:var(--white);position:relative}
a{color:inherit;text-decoration:none}
.btn{display:inline-block;background:var(--navy);color:#fff;font-family:"Exo 2",sans-serif;font-weight:700;font-size:13px;letter-spacing:.5px;padding:9px 20px;text-transform:uppercase}
.btn-ghost{background:transparent;border:2px solid #fff;padding:6px 20px}
.wordmark{display:flex;align-items:center;gap:10px;font-family:"Exo 2",sans-serif;font-weight:700;color:var(--navy);font-size:20px}
.wordmark .dot{width:22px;height:22px;border-radius:50%;background:var(--navy)}
.site-header{position:absolute;top:0;left:0;width:1200px;height:120px;background:linear-gradient(#fff,#f0f0f0);display:flex;align-items:center;justify-content:space-between;padding:0 110px}
.nav{display:flex;gap:8px;font-family:"Exo 2",sans-serif;font-weight:600;font-size:14px;color:#444}
.nav a{padding:8px 14px}
.nav a.active{background:var(--navy);color:#fff}
.hero{position:absolute;top:120px;left:0;width:1200px;height:520px}
.hero-photo{position:absolute;inset:0;background:linear-gradient(90deg,#e6e9ee 0%,#dfe3e8 55%,#c9ced6 70%,#9aa1ad 85%,#d8dbe0 100%)}
.hero-text{position:absolute;left:210px;top:158px;width:440px;text-align:center}
.hero-text h1{font-family:"Exo 2",sans-serif;font-weight:700;color:var(--navy);font-size:29px;margin-bottom:10px}
.hero-text blockquote{font-family:"Exo 2",sans-serif;font-size:18px;line-height:32px;color:#333;font-weight:500}
.hero-text cite{display:block;font-style:normal;font-family:"Exo 2",sans-serif;font-weight:700;color:var(--navy);font-size:14px;margin:4px 0 14px}
.hero-dots{position:absolute;top:460px;left:552px;display:flex;gap:18px}
.hero-dots span{width:10px;height:10px;border-radius:50%;background:#7a7f88}
.hero-dots span.on{background:var(--navy)}
.section-head{text-align:center}
.section-head .mark{width:14px;height:14px;background:var(--navy);margin:0 auto 10px;border-radius:50%}
.section-head h2{font-family:"Exo 2",sans-serif;font-weight:700;font-size:26px;color:var(--navy)}
.rule{width:180px;height:1px;background:var(--navy);margin:6px auto 0;position:relative}
.rule::after{content:"• • • • •";position:absolute;left:50%;top:2px;transform:translateX(-50%);font-size:8px;letter-spacing:1px;color:var(--navy);background:inherit}
.revenue{position:absolute;top:640px;left:0;width:1200px;height:375px;background:var(--soft);padding-top:20px;text-align:center}
.revenue .rule::after{background:var(--soft)}
.revenue .copy{width:880px;margin:22px auto 0;font-size:12.5px;line-height:20px;color:#333}
.revenue .copy p{margin-bottom:20px}
.revenue .btn{margin-top:6px}
.services{position:absolute;top:1025px;left:0;width:1200px;height:650px;background:#fff;padding-top:46px;text-align:center}
.services .rule::after{background:#fff}
.services .lead{width:900px;margin:28px auto 0;font-size:12.5px;line-height:20px;color:#333}
.services h3{font-family:"Ubuntu",sans-serif;font-weight:400;font-size:17px;margin-top:20px;color:#222}
.cards{position:absolute;top:261px;left:150px;display:flex;gap:42px}
.card{width:272px;height:320px;background:var(--navy);color:#fff;padding-top:38px}
.card.alt{background:var(--card-soft);color:#333}
.card h4{font-family:"Exo 2",sans-serif;font-weight:500;font-size:17px;margin-bottom:22px}
.card.alt h4{color:var(--navy)}
.card svg{display:block;margin:0 auto 22px}
.card ul{list-style:none;font-size:12px;line-height:20px}
.about{position:absolute;top:1675px;left:0;width:1200px;height:910px;color:#fff;text-align:center}
.about-photo{position:absolute;inset:0;background:linear-gradient(160deg,#2b5a99 0%,#1f4c8a 45%,#2a5b9c 70%,#1a437f 100%)}
.about-inner{position:relative;padding-top:38px}
.about .section-head h2{color:#fff}
.about .section-head .mark{background:#fff}
.about .rule{background:#fff}
.about .rule::after{color:#fff;background:#21508f}
.about .intro{width:880px;margin:34px auto 0;font-size:15.5px;line-height:21px}
.about .intro-small{width:920px;margin:14px auto 22px;font-size:11.5px;line-height:20px}
.team{position:absolute;top:360px;left:168px;width:868px;display:grid;grid-template-columns:402px 402px;column-gap:64px;row-gap:40px;text-align:left}
.team::before{content:"";position:absolute;left:432px;top:0;width:1px;height:520px;background:rgba(255,255,255,.35)}
.member h5{font-family:"Exo 2",sans-serif;font-weight:700;font-size:16px;line-height:20px;text-transform:uppercase;min-height:40px}
.member p{font-size:11.5px;line-height:20px;margin:8px 0 16px;height:100px;overflow:hidden}
.member .btn{font-size:12px}
.newsletter{position:absolute;top:2585px;left:0;width:1200px;height:150px;background:var(--news);display:flex;align-items:center;padding-left:166px}
.newsletter h2{font-family:"Exo 2",sans-serif;font-weight:500;color:#fff;font-size:24px;letter-spacing:1px;width:324px}
.email{width:366px;height:40px;background:#fff;display:flex;align-items:center;justify-content:space-between;padding:0 14px;font-size:11px;color:#333}
.newsletter .btn{width:168px;height:40px;margin-left:6px;font-size:15px;text-align:center;padding-top:11px;background:var(--navy-dark)}
.site-footer{position:absolute;top:2735px;left:0;width:1200px;height:220px;background:var(--footer);padding:36px 0 0 166px;display:flex}
.site-footer h6{font-family:"Exo 2",sans-serif;font-weight:700;color:var(--navy);font-size:15px;margin-bottom:16px}
.links{width:348px}
.links ul{list-style:none;font-size:12px;color:#333}
.links li{margin-bottom:17px;display:flex;align-items:center;gap:14px}
.links li::before{content:"★";color:var(--navy);font-size:11px}
.contact{width:368px;font-size:12px;color:#333}
.contact div{display:flex;gap:12px;margin-bottom:22px;line-height:18px}
.social .icons{display:flex;gap:4px;margin-bottom:24px}
.social .icons span{width:26px;height:26px;border-radius:50%}
.copy-bar{position:absolute;top:2955px;left:0;width:1200px;height:50px;background:var(--copy);text-align:center;font-size:12px;line-height:50px;color:#333}
</style>
</head>
<body>
<header class="site-header">
  <div class="wordmark"><span class="dot"></span>Bright Meridian Partners</div>
  <nav class="nav"><a class="active" href="#">HOME</a><a href="#">ABOUT</a><a href="#">SERVICES</a><a href="#">CONTACT US</a></nav>
</header>

<section class="hero">
  <div class="hero-photo" role="img" aria-label="Photo of a smiling consultant wearing a headset, arms crossed, in a bright office"></div>
  <div class="hero-text">
    <h1>BRIGHT MERIDIAN PARTNERS</h1>
    <blockquote>“AGILITY IS THE KEY TO BUILDING A BUSINESS THAT IS FASTER – AND MORE PROFITABLE – THAN THE COMPETITION”</blockquote>
    <cite>PAUL EVERLY</cite>
    <a class="btn" href="#">LEARN MORE</a>
  </div>
  <div class="hero-dots"><span></span><span></span><span class="on"></span><span></span></div>
</section>

<section class="revenue">
  <div class="section-head"><div class="mark"></div><h2>WE SIMPLY ACCELERATE REVENUE</h2><div class="rule"></div></div>
  <div class="copy">
    <p>Our Clients choose us to help them move faster and be more competitive in an On-Demand World.</p>
    <p>Accelerating revenue and profit often cannot always be solved internally for a variety of reasons, from capability, culture, politics and an internal lens. We have an independent perspective to to accelerate performance and turn strategy into action fast.</p>
    <p>Whether it be an improved strategic vision with leadership coaching, facilitating workshops to unlock consumer and customer partnerships, sales and negotiation trainingor improving supply chain efficiencies, our exec team work to closely embed ourselves within our clients.</p>
    <p>We offer an agile solution with tailored products for accelerated growth. We have lived it to simply make it happen for you.</p>
  </div>
  <a class="btn" href="#">READ MORE</a>
</section>

<section class="services">
  <div class="section-head"><div class="mark"></div><h2>OUR SERVICES</h2><div class="rule"></div></div>
  <p class="lead">Whether you have the need to unlock the strategic vision to keep pace in the market, improve your customer and consumer relevance, help make the business move faster at an operational level, simplify the processes to get focus, refine the way you go to market, sell, negotiate and create high performing teams.....</p>
  <h3>Bright Meridian Partners will help you win</h3>
  <div class="cards">
    <div class="card">
      <h4>STRATEGIC FOCUS</h4>
      <svg width="70" height="66" viewBox="0 0 70 66" fill="none" stroke="#fff" stroke-width="2.5"><circle cx="32" cy="36" r="26"/><circle cx="32" cy="36" r="17"/><circle cx="32" cy="36" r="8"/><path d="M32 36 60 8M52 8h8v8"/></svg>
      <ul><li>Strategic Joined Up Business Planning</li><li>Coaching C Suite &amp; Below</li><li>Creating High Performing Teams</li><li>Facilitating Workshops</li></ul>
    </div>
    <div class="card alt">
      <h4>CUSTOMER FOCUS</h4>
      <svg width="70" height="66" viewBox="0 0 70 66" fill="none" stroke="#1c4886" stroke-width="2.5"><circle cx="35" cy="33" r="27"/><path d="M35 2v10M35 54v10M4 33h10M56 33h10"/><circle cx="24" cy="30" r="5"/><circle cx="35" cy="27" r="5"/><circle cx="46" cy="30" r="5"/><path d="M16 44c2-6 14-6 16 0M27 42c2-7 14-7 16 0M38 44c2-6 14-6 16 0"/></svg>
      <ul><li>Unlocking Strategic Customer Partner-</li><li>ships. Selling and Negotiation</li><li>Trading Terms Strategies &amp; Investment</li></ul>
    </div>
    <div class="card">
      <h4>CONSUMER FOCUS</h4>
      <svg width="70" height="66" viewBox="0 0 70 66" fill="none" stroke="#fff" stroke-width="2.5"><path d="M22 62V50c-8-4-12-12-12-20 0-14 11-25 25-25s25 11 25 25l6 10h-6v10H50v10"/><circle cx="34" cy="28" r="7"/><path d="M34 14v6M34 36v6M20 28h6M42 28h6M24 18l4 4M40 34l4 4M24 38l4-4M40 22l4-4"/></svg>
      <ul><li>Consumer Pricing Strategies</li><li>Consumer Insights</li><li>Category Management</li></ul>
    </div>
  </div>
</section>

<section class="about">
  <div class="about-photo" role="img" aria-label="Blue-toned photo of a team working together over documents"></div>
  <div class="about-inner">
    <div class="section-head"><div class="mark"></div><h2>ABOUT US</h2><div class="rule"></div></div>
    <p class="intro">We are not consultants in the true definition of the word, rather we are a proven team off experts. Being a trusted and net-worked team who have lived and breathed the consumer goods industry, we are passionate about our brand, and about helping our clients to unlock their true potential for themselves and shareholders</p>
    <p class="intro-small">Bright Meridian Partners was founded in January 2017 as there was a clear gap in the consumer goods and services market for a boutique group of experts to support execution of strategies to accelerate revenue.</p>
    <a class="btn btn-ghost" href="#">READ MORE</a>
  </div>
  <div class="team">
    <article class="member">
      <h5>Robert Calder, Managing Director , Bright Meridian Partners</h5>
      <p>Robert Calder is an accomplished sales executive with nearly 20 years' experience in various leadership roles across some of the UK and Australia's premier retail and FMCG companies including Kestrel Toys, Lumina Beauty, and Northgate Consumer Co working to drive profit and revenue growth with leading retailers worldwide.</p>
      <a class="btn btn-ghost" href="#">READ MORE</a>
    </article>
    <article class="member">
      <h5>James Harlow, Associate Sales and Mktg Strategy, Bright Meridian Partners</h5>
      <p>James is a proven FMCG Senior Executive with 20+ years of experience in a number of key leadership roles across Greenvale Dairy, Kestrel Toys, Vellamy Estate Wines. James has been instrumental in forging global strategy, Sales and Category Management leadership roles in Australia and internationally.</p>
      <a class="btn btn-ghost" href="#">READ MORE</a>
    </article>
    <article class="member">
      <h5>Thomas Delane, Associate Supply Chain Strategy &amp; Logistics, Bright Meridian Partners</h5>
      <p>Thomas has been consulting to FMCG and publicly listed companies in Australia for the past eight years after thirty years in senior management roles in major multi-national and Australian food companies including Corvo Foods, Greenvale Dairy, Fizzline Snacks. With management and consulting assignments in supply chain strategy, improvement of supply chains and improving organisa-</p>
      <a class="btn btn-ghost" href="#">READ MORE</a>
    </article>
    <article class="member">
      <h5>Olena Prescott, Associate Leadership &amp; Strategy, Coach/ Facilitator, Bright Meridian Partners</h5>
      <p>Olena brings 20 years' hands on executive, coaching and consulting track record across industries and the globe. Having worked with C-Suite | Boards, rising top talent, entrepreneurs and cross-company partnerships – in one-to-one and team sessions using a customised approach backed by wisdom of psychology, business and creativity, Olena is a valued member</p>
      <a class="btn btn-ghost" href="#">READ MORE</a>
    </article>
  </div>
</section>

<section class="newsletter">
  <h2>NEWSLETTER SUBSCRIBE</h2>
  <div class="email"><span>ENTER EMAIL ID</span><svg width="16" height="12" viewBox="0 0 16 12" fill="none" stroke="#555" stroke-width="1.3"><rect x=".7" y=".7" width="14.6" height="10.6"/><path d="M1 1l7 6 7-6"/></svg></div>
  <a class="btn" href="#">SUBSCRIBE</a>
</section>

<footer class="site-footer">
  <div class="links"><h6>QUICK LINKS</h6><ul><li>HOME</li><li>ABOUT US</li><li>SERVICES</li><li>CONTACT US</li></ul></div>
  <div class="contact"><h6>CONTACT US</h6>
    <div><svg width="12" height="16" viewBox="0 0 12 16"><path d="M6 0a6 6 0 0 0-6 6c0 4.5 6 10 6 10s6-5.5 6-10a6 6 0 0 0-6-6zm0 8.5A2.5 2.5 0 1 1 6 3.5a2.5 2.5 0 0 1 0 5z" fill="#333"/></svg><span>Suite 12, 48 Harbour Lane<br>Eastbrook</span></div>
    <div><svg width="14" height="14" viewBox="0 0 14 14"><path d="M3 0l3 3-2 2c1 2 3 4 5 5l2-2 3 3-2 3C6 14 0 8 0 2z" fill="#333"/></svg><span>(555)-010-2847</span></div>
    <div><svg width="14" height="11" viewBox="0 0 14 11"><rect width="14" height="11" fill="#333"/><path d="M0 0l7 6 7-6" stroke="#ececec" fill="none"/></svg><span>hello@brightmeridian.example</span></div>
  </div>
  <div class="social"><h6>FOLLOW US</h6>
    <div class="icons"><span style="background:#1c4886"></span><span style="background:#2a9fd8"></span><span style="background:#c8232c"></span><span style="background:#1a6fb0"></span><span style="background:#dc4a38"></span></div>
    <div class="wordmark" style="font-size:16px"><span class="dot" style="width:16px;height:16px"></span>Bright Meridian Partners</div>
  </div>
</footer>
<div class="copy-bar">Copyrights © 2017 - All Rights Reserved</div>
</body>
</html>
```